high-impact, conversion-focused website redesign for the government sector

Objective: To design and develop a high-impact, conversion-focused digital platform that solidifies Harrowgate Lumen Advisors (HLA) as the leading communications and strategy firm for government, defense, and industrial clients. The site must project authority, innovation, and sophisticated precision. See the creative breif for more information

Target Market(s)

Government contractors

Industry/Entity Type

Government, defense, industrials

Coding

Coded - Design and coding required

Number of Pages Required

5+ page

Font styles to use
Other font styles liked:
• See the current website

Requirements
Must have
• See design brief
Nice to have
• See design brief
Should not have
• See design brief

```html
<!DOCTYPE html>
<html lang="en">
<head>
<meta charset="utf-8">
<title>Harrowgate Lumen Advisors — Accelerate Your Mission</title>
<link href="https://fonts.googleapis.com/css2?family=Michroma&family=Lexend:wght@300;400;500;600;700&display=swap" rel="stylesheet">
<style>
:root{
  --green:#8cc63f;
  --green-dark:#5f9a2a;
  --ink:#111418;
  --text:#2a2d31;
  --muted:#5a5e63;
  --card:#efefef;
  --navy:#1f4e79;
  --blue:#2f8fe0;
  --orange:#f5a623;
  --footer:#101215;
  --white:#ffffff;
}
*{margin:0;padding:0;box-sizing:border-box}
html,body{width:1200px;height:4799px;overflow:hidden}
body{position:relative;background:var(--white);font-family:'Lexend',sans-serif;color:var(--text)}
.abs{position:absolute}
.display{font-family:'Michroma',sans-serif;font-weight:400}
.btn{position:absolute;display:flex;align-items:center;justify-content:center;font-size:12px;text-transform:uppercase;letter-spacing:.3px}
.btn-green{background:var(--green);color:var(--white)}
.btn-outline{border:1.5px solid var(--ink);color:var(--ink);border-radius:3px}
.btn-outline-light{border:1.5px solid var(--white);color:var(--white);border-radius:3px}

/* Hero */
.hero{left:0;top:0;width:1200px;height:568px;background:radial-gradient(ellipse at 70% 40%,#5a6a72 0%,#37444c 45%,#1e2830 100%)}
.brand{display:flex;align-items:center;gap:10px}
.brand-mark{width:22px;height:22px;background:var(--green);flex:none}
.brand-name{font-family:'Lexend',sans-serif;font-weight:500;font-size:15px;line-height:1.15;letter-spacing:.6px;text-transform:uppercase;color:var(--white);width:170px}
.nav{left:661px;top:58px;display:flex;gap:20px;font-size:11px;color:var(--white);text-transform:uppercase;letter-spacing:.3px}
.hero-title{left:112px;top:208px;font-size:56px;line-height:65px;color:var(--white)}
.hero-copy{left:119px;top:357px;width:560px;font-size:13.5px;line-height:22px;color:var(--white);font-weight:300}

.intro{left:200px;top:608px;width:800px;text-align:center;font-size:22px;line-height:34px;font-weight:600;color:var(--ink)}

.photo-jets{left:0;top:760px;width:1057px;height:406px;background:linear-gradient(135deg,#1d2a33 0%,#3c4d57 45%,#52656e 70%,#2a3841 100%)}
.team-card{left:602px;top:876px;width:525px;height:369px;background:var(--card);padding:42px 44px}
.team-card h3{font-size:18.5px;line-height:27px;font-weight:600;color:var(--ink)}
.team-card p{margin-top:24px;font-size:12.5px;line-height:24px;color:var(--text);font-weight:300}
.team-card .btn{position:static;margin-top:14px;width:112px;height:34px}

.results-title{left:116px;top:1326px;font-size:31px;line-height:38px;color:var(--ink)}
.results-copy{left:589px;top:1328px;width:480px;font-size:13px;line-height:24px;font-weight:300;color:var(--text)}
.stat{top:1508px;width:300px;text-align:center}
.stat-num{font-family:'Michroma',sans-serif;font-size:50px;color:var(--green);line-height:70px}
.stat-label{margin-top:24px;font-size:14px;line-height:20px;font-weight:300;color:var(--text)}
.divider{top:1520px;width:1px;height:160px;background:#d9d9d9}

/* Testimonials */
.testimonials{left:0;top:1729px;width:1200px;height:525px;background:linear-gradient(180deg,#0a0d10 0%,#222b30 50%,#3a4636 100%)}
.quote{left:170px;top:1972px;width:860px;text-align:center;color:var(--white);font-size:17px;line-height:32px;font-weight:300}
.dots{left:540px;top:2185px;width:120px;display:flex;justify-content:center;gap:8px;align-items:center}
.dot{width:11px;height:11px;border-radius:50%;background:var(--white)}
.dot.active{width:14px;height:14px;background:transparent;border:2px solid var(--white)}

/* Services */
.services-title{left:0;top:2305px;width:1200px;text-align:center;font-size:31px;color:var(--ink)}
.service{width:234px;height:88px;border:1px solid #ececec;display:flex;align-items:center;gap:18px;padding-left:16px;font-size:14px;font-weight:500;line-height:19px;color:var(--ink)}
.service-icon{width:58px;height:58px;border-radius:8px;background:#e6f1d8;flex:none}

/* Edge */
.edge{left:0;top:2688px;width:1200px;height:537px;background:linear-gradient(135deg,#1e2b22 0%,#35503a 40%,#2a3e31 70%,#17211b 100%)}
.edge-lead{left:107px;top:2874px;width:440px;font-size:21px;line-height:27px;font-weight:600;color:var(--white)}
.edge-copy{left:107px;top:3006px;width:400px;font-size:13px;line-height:24px;font-weight:300;color:var(--white)}
.edge-frame{left:440px;top:3045px;width:105px;height:130px;border-right:2px solid var(--white);border-bottom:2px solid var(--white)}

/* Expect */
.expect-title{left:0;top:3268px;width:1200px;text-align:center;font-size:36px;font-weight:600;color:var(--ink)}
.expect-copy{left:240px;top:3350px;width:740px;text-align:center;font-size:13.5px;line-height:24px;font-weight:300;color:var(--text)}
.brand-wheel{left:205px;top:3500px;width:380px;height:380px;border-radius:50%;background:conic-gradient(from 0deg,#2f8fe0 0 25%,#f5a623 25% 50%,#7cb342 50% 75%,#4f8a2b 75% 100%);opacity:.85}
.expect-body{left:613px;top:3505px;width:458px;font-size:13.5px;line-height:24px;font-weight:300;color:var(--text)}
.expect-body p+p{margin-top:24px}

/* Insights */
.eyebrow{left:116px;top:3995px;font-size:12px;color:var(--green);text-transform:uppercase;letter-spacing:.4px}
.insights-title{left:116px;top:4040px;font-size:30px;line-height:46px;color:var(--ink)}
.see-all{left:948px;top:4050px;font-size:12px;color:var(--green);font-weight:600;text-transform:uppercase}
.article{top:4164px;width:311px}
.article-photo{height:208px}
.article p{margin-top:20px;font-size:13px;line-height:20px;font-weight:500;color:var(--ink);padding:0 4px}
.article a{display:block;margin-top:14px;padding:0 4px;font-size:11px;color:var(--green);font-weight:600;text-decoration:none;text-transform:uppercase}
.arrow{top:4265px;width:20px;height:28px}

/* Footer */
.footer{left:0;top:4508px;width:1200px;height:291px;background:var(--footer);color:var(--white)}
.footer h4{font-family:'Michroma',sans-serif;font-weight:400;font-size:12px;letter-spacing:.4px;text-transform:uppercase}
.footer ul{list-style:none;margin-top:26px;font-size:12px;line-height:22.5px;font-weight:300}
.social{display:flex;gap:10px}
.social span{width:28px;height:28px;border-radius:50%;background:var(--green)}
.contact-row{display:flex;align-items:center;gap:14px;font-size:12px;font-weight:300}
.contact-icon{width:24px;height:24px;border-radius:50%;background:var(--green);flex:none;display:flex;align-items:center;justify-content:center}
.copyright{left:0;top:4762px;width:1200px;text-align:center;font-size:11px;font-weight:300;color:#c9c9c9}
</style>
</head>
<body>

<!-- Hero -->
<section class="abs hero" role="img" aria-label="Aerial photograph of farmland and clouds seen from high altitude"></section>
<div class="abs brand" style="left:115px;top:34px">
  <span class="brand-mark"></span>
  <span class="brand-name">Harrowgate Lumen Advisors</span>
</div>
<nav class="abs nav"><span>Home</span><span>Advisory Services</span><span>About Us</span><span>Blog</span><span>Contact Us</span></nav>
<h1 class="abs hero-title display">ACCELERATE<br>YOUR MISSION</h1>
<p class="abs hero-copy">Harrowgate Lumen Advisors exists for one reason to help connect the federal ecosystem with the technologies that matter most to America and her allies.</p>
<a class="btn btn-green" style="left:119px;top:423px;width:125px;height:31px">Contact Us</a>

<p class="abs intro">We help build the communications, government affairs and marketing strategies and systems your organization needs to grow and protect market share –helping our clients meet their mission objectives.</p>

<div class="abs photo-jets" role="img" aria-label="Aerial photograph of an airliner taking off over a busy airport apron"></div>
<div class="abs team-card">
  <h3>Our team of award-winning communications strategists bring deep experience across government, defense, and technology.</h3>
  <p>We build systems, teams, and strategies that drive outcomes for federal contractors and innovators supporting national security, space, and industrial growth. Our team has served in the military, supported the DoD and federal leaders, and led communications, marketing, and government affairs for major government, tech and investment organizations.</p>
  <a class="btn btn-outline">Learn More</a>
</div>

<h2 class="abs results-title display">PROVEN RESULTS<br>THAT DRIVE REAL<br>GROWTH</h2>
<p class="abs results-copy">We've helped brands strengthen their digital presence, expand their network, and accelerate opportunities across the defense, space, and government sectors. In just one year, our clients have achieved:</p>

<div class="abs stat" style="left:131px"><div class="stat-num">+72%</div><p class="stat-label">Increase in database contacts through CRM implementation and targeted marketing campaigns</p></div>
<div class="abs divider" style="left:451px"></div>
<div class="abs stat" style="left:455px"><div class="stat-num">100+</div><p class="stat-label">Introductions to tech-scouting contracts across the DoD and the aerospace &amp; defense ecosystem</p></div>
<div class="abs divider" style="left:779px"></div>
<div class="abs stat" style="left:791px"><div class="stat-num">570%</div><p class="stat-label">Positioned a client for transformative growth, fueling a 570% increase in stock price and attracting $50M AUD in new investment</p></div>

<!-- Testimonials -->
<section class="abs testimonials" role="img" aria-label="Dark aerial photograph of forested land at dusk"></section>
<svg class="abs" style="left:0;top:1780px" width="1200" height="125" viewBox="0 0 1200 125">
  <text x="10" y="112" font-family="Michroma, sans-serif" font-size="128" fill="#ffffff" textLength="1180" lengthAdjust="spacingAndGlyphs">TESTIMONIALS</text>
</svg>
<p class="abs quote">“Partnering with Harrowgate Lumen Advisors accelerated the growth of our company. Their strategic insight, deep federal expertise, and hands-on support transformed our U.S. expansion. In less than six months, they built our presence in the United States from the ground up, helping us secure contracts, advocates, and visibility at the highest levels. Working with Harrowgate Lumen Advisors has been a true game-changer for our company.”</p>
<div class="abs dots"><span class="dot"></span><span class="dot active"></span><span class="dot"></span></div>

<!-- Services -->
<h2 class="abs services-title display">SERVICES WE OFFER</h2>
<div class="abs service" style="left:116px;top:2397px"><span class="service-icon" role="img" aria-label="Corporate building icon"></span>Corporate<br>Communications</div>
<div class="abs service" style="left:360px;top:2397px"><span class="service-icon" role="img" aria-label="Network of people icon"></span>Public Relations</div>
<div class="abs service" style="left:604px;top:2397px"><span class="service-icon" role="img" aria-label="Group handshake icon"></span>Government<br>Affairs</div>
<div class="abs service" style="left:848px;top:2397px"><span class="service-icon" role="img" aria-label="Alert gear icon"></span>Crisis<br>Communications</div>
<div class="abs service" style="left:116px;top:2492px"><span class="service-icon" role="img" aria-label="Growth chart icon"></span>Digital Marketing</div>
<div class="abs service" style="left:360px;top:2492px"><span class="service-icon" role="img" aria-label="Strategy figures icon"></span>Strategic<br>Connections</div>
<div class="abs service" style="left:604px;top:2492px"><span class="service-icon" role="img" aria-label="Investor meeting icon"></span>Investor<br>Relations</div>
<div class="abs service" style="left:848px;top:2492px"><span class="service-icon" role="img" aria-label="Calendar icon"></span>Event<br>Management</div>
<a class="btn btn-outline" style="left:550px;top:2608px;width:111px;height:36px">View All</a>

<!-- Our Edge -->
<section class="abs edge" role="img" aria-label="Satellite photograph of green mountain terrain"></section>
<svg class="abs" style="left:0;top:2730px" width="1200" height="95" viewBox="0 0 1200 95">
  <text x="142" y="84" font-family="Michroma, sans-serif" font-size="86" fill="#ffffff" textLength="958" lengthAdjust="spacing">OUREDGE</text>
</svg>
<p class="abs edge-lead">We combine deep federal sector insight, technical understanding, and a powerful network across government, industry, investors, and media.</p>
<div class="abs edge-frame"></div>
<p class="abs edge-copy">Our proven approach drives results — from major contract wins and successful M&amp;A to increased valuation, strategic investment, and political support. Our strategies begin with your mission and business goals, ensuring every message, relationship, and action advances growth and impact.</p>
<a class="btn btn-outline-light" style="left:112px;top:3147px;width:111px;height:34px">Learn More</a>

<!-- What to expect -->
<svg class="abs" style="left:0;top:3290px" width="1200" height="620" viewBox="0 0 1200 620">
  <polygon points="0,80 330,110 186,240 186,540 0,580" fill="var(--navy)"/>
  <polygon points="1200,10 1200,270 1085,270" fill="var(--green)"/>
</svg>
<h2 class="abs expect-title">What to Expect When Partnering with Us</h2>
<p class="abs expect-copy">With decades of experience, a results-focused methodology, and cutting-edge marketing and communications tools and technologies, we begin every engagement with a discovery and planning process to ensure we are building a strategy that cuts through the noise to achieve our measurable results.</p>

<div class="abs brand-wheel" role="img" aria-label="Brand development wheel illustration showing messaging and connections, building brands, government affairs and marketing around a central brand"></div>

<div class="abs expect-body">
  <p>As specialists in government crisis communications, we additionally examine our client's current strategy for risks ensuring we are building on a stable foundation.</p>
  <p>By truly understanding our client's goals, key milestones, potential areas of risk, ideal customer and investor targets, partner profiles, and other key drivers, we create messaging and strategy that goes beyond traditional brand awareness to meet mission objectives. As a full service firm, we work across all the areas in the graphic.</p>
  <p>Our time-tested methodology is based on building and executing a strategy aligned with client mission objectives. With the strategy in place, we execute tactics with precision, efficiency, and the highest quality of customer service.</p>
</div>

<!-- Insights -->
<span class="abs eyebrow">Latest Insights</span>
<h2 class="abs insights-title display">STAY INFORMED, STAY AHEAD:<br>YOUR SOURCE FOR BREAKING NEWS.</h2>
<span class="abs see-all">See All Articles</span>

<svg class="abs arrow" style="left:70px" viewBox="0 0 20 28"><polyline points="15,4 5,14 15,24" fill="none" stroke="#111418" stroke-width="2.5"/></svg>
<svg class="abs arrow" style="left:1128px" viewBox="0 0 20 28"><polyline points="5,4 15,14 5,24" fill="none" stroke="#111418" stroke-width="2.5"/></svg>

<article class="abs article" style="left:116px">
  <div class="article-photo" role="img" aria-label="Aerial photograph of a rural town among fields" style="background:linear-gradient(160deg,#8a9a7a,#5d6e55 55%,#3d4a38)"></div>
  <p>As specialists in government crisis communications, we additionally</p>
  <a>+ Learn More</a>
</article>
<article class="abs article" style="left:449px">
  <div class="article-photo" role="img" aria-label="Aerial photograph of suburban housing" style="background:linear-gradient(160deg,#9fa8a0,#6b7a6a 55%,#45503f)"></div>
  <p>As specialists in government crisis communications, we additionally</p>
  <a>+ Learn More</a>
</article>
<article class="abs article" style="left:782px">
  <div class="article-photo" role="img" aria-label="Aerial photograph of clouds over farmland" style="background:linear-gradient(160deg,#c2c8cb,#7d8a8f 50%,#3e4a50)"></div>
  <p>As specialists in government crisis communications, we additionally</p>
  <a>+ Learn More</a>
</article>

<!-- Footer -->
<footer class="abs footer">
  <div class="abs brand" style="left:116px;top:58px">
    <span class="brand-mark"></span>
    <span class="brand-name" style="font-size:17px;width:200px">Harrowgate Lumen Advisors</span>
  </div>
  <div class="abs social" style="left:176px;top:140px"><span role="img" aria-label="Social profile"></span><span role="img" aria-label="Social profile"></span></div>

  <div class="abs" style="left:395px;top:26px">
    <h4>Navigation</h4>
    <ul><li>Home</li><li>Advisory Services</li><li>About Us</li><li>Blog</li><li>Contact Us</li></ul>
  </div>
  <div class="abs" style="left:570px;top:26px">
    <h4>Services We Offer</h4>
    <ul><li>Corporate Communications</li><li>Public Relations</li><li>Government Affairs</li><li>Crisis Communications</li><li>Digital Marketing</li><li>Strategic Connections</li><li>Investor Relations</li><li>Event Management</li></ul>
  </div>
  <div class="abs" style="left:872px;top:26px">
    <h4>Contact Us</h4>
    <div class="contact-row" style="margin-top:30px;font-size:17px;font-weight:600">
      <span class="contact-icon"><svg width="13" height="13" viewBox="0 0 24 24"><path d="M6.6 10.8a15 15 0 0 0 6.6 6.6l2.2-2.2c.3-.3.7-.4 1-.2 1.1.4 2.3.6 3.6.6.6 0 1 .4 1 1V20c0 .6-.4 1-1 1A17 17 0 0 1 3 4c0-.6.4-1 1-1h3.5c.6 0 1 .4 1 1 0 1.3.2 2.5.6 3.6.1.3 0 .7-.2 1z" fill="#fff"/></svg></span>555-014-2290
    </div>
    <div class="contact-row" style="margin-top:14px;text-decoration:underline">
      <span class="contact-icon"><svg width="13" height="13" viewBox="0 0 24 24"><rect x="3" y="6" width="18" height="12" fill="none" stroke="#fff" stroke-width="2"/><polyline points="3,6 12,13 21,6" fill="none" stroke="#fff" stroke-width="2"/></svg></span>info@harrowgatelumen.com
    </div>
    <div class="contact-row" style="margin-top:12px;font-size:11px;line-height:16px">
      <span class="contact-icon"><svg width="13" height="13" viewBox="0 0 24 24"><path d="M12 2a7 7 0 0 0-7 7c0 5 7 13 7 13s7-8 7-13a7 7 0 0 0-7-7zm0 9.5A2.5 2.5 0 1 1 12 6.5a2.5 2.5 0 0 1 0 5z" fill="#fff"/></svg></span>2210 Corvel Avenue Fairhaven,<br>Illinois 60411
    </div>
  </div>
</footer>
<p class="abs copyright">© 2025 Harrowgate Lumen Advisors. All rights reserved.</p>

</body>
</html>
```